Bulldog themed background for Real Estate Purchase Letter

I need a phantom background or watermark on a standard 8 1/2" x 11" paper. I am going to put a letter over the background. I want a bulldog theme that is cute, funny and original. This letter is for a real estate project and we want to capture the person sub-consciously . Attached is my personal dogs. If you want to use them you can but not required. I have attached the letter that I am trying to emulate. I want bulldogs not horses.

Target Market(s)

45 years old and higher

Industry/Entity Type

Real Estate

Font styles to use
Serif
Sans Serif

Colors

Designer to choose colors to be used in the design.

Requirements
Must have
• fun, happiness, reassuring,
Should not have
• violence, negativity, unhappy

```html
<!DOCTYPE html>
<html lang="en">
<head>
<meta charset="utf-8">
<title>Purchase Letter – Licensed Real Estate Agent</title>
<link rel="stylesheet" href="https://fonts.googleapis.com/css2?family=Questrial&family=Roboto:wght@400;500;700&family=EB+Garamond:wght@500&display=swap">
<style>
  :root{
    --backdrop:#e4e4e4;
    --paper-light:#f4f4f4;
    --paper-dark:#dcdcdc;
    --brand-blue:#0050c8;
    --ink:#2b2b2b;
    --ink-soft:#555555;
    --name-blue:#1d4f9a;
    --dog-white:#e9e6e2;
    --dog-shade:#b9a89a;
  }
  *{box-sizing:border-box;margin:0;padding:0}
  html,body{width:1024px;height:1200px;overflow:hidden;background:var(--backdrop)}
  .letter{
    position:absolute;left:112px;top:41px;width:800px;height:1118px;
    background:linear-gradient(100deg,var(--paper-light) 0%,var(--paper-dark) 100%);
    overflow:hidden;
    box-shadow:0 6px 18px rgba(0,0,0,.18);
    color:var(--ink);
  }
  .letter__swoosh{position:absolute;left:0;top:0;width:800px;height:1118px}
  .letter__block{position:absolute;font-family:"Roboto",sans-serif}
  .recipient{left:85px;top:122px;font-size:15.5px;line-height:22px}
  .recipient__address{margin-top:21px}
  .sender-title{left:448px;top:119px;font-size:19.5px;font-weight:500}
  .letter__body{
    position:absolute;left:85px;top:263px;width:638px;
    font-family:"Questrial",sans-serif;font-size:13.8px;line-height:25.2px;
    text-align:justify;hyphens:auto;color:var(--ink)
  }
  .letter__body p{margin-bottom:25.2px}
  .letter__body .salutation{margin-bottom:25.2px}
  .letter__body strong{font-weight:700;font-family:"Roboto",sans-serif;font-size:13.4px}
  .letter__closing{position:absolute;left:85px;top:769px;font-family:"Questrial",sans-serif;font-size:13.8px}
  .signature-mark{position:absolute;left:85px;top:802px;width:104px;height:38px;
    background:linear-gradient(90deg,rgba(29,79,154,.25),rgba(29,79,154,.08));border-radius:4px}
  .signer{position:absolute;left:85px;top:857px}
  .signer__name{font-family:"EB Garamond",serif;font-size:23px;font-weight:500;color:var(--name-blue);line-height:30px}
  .signer__phone{font-family:"Roboto",sans-serif;font-size:15.5px;color:var(--ink-soft);margin-top:6px}
  .postscript{left:85px;top:951px;font-size:15.5px;line-height:25.5px}
  .mascot-photo{
    position:absolute;left:576px;top:856px;width:212px;height:258px;border-radius:40% 40% 12% 12%;
    background:radial-gradient(circle at 45% 35%,var(--dog-white) 0%,#d7cfc8 55%,var(--dog-shade) 100%);
  }
</style>
</head>
<body>
  <main class="letter">
    <svg class="letter__swoosh" viewBox="0 0 800 1118" aria-hidden="true">
      <path d="M0 0 H310 C190 30 60 90 0 170 Z" fill="var(--brand-blue)"/>
      <path d="M800 900 C700 1010 540 1090 369 1118 H800 Z" fill="var(--brand-blue)"/>
    </svg>

    <div class="letter__block recipient">
      <div>Mr Outta State Owner</div>
      <div class="recipient__address">4821 HarborLane,<br>LAKEVIEW FL 34012 1187</div>
    </div>
    <div class="letter__block sender-title">Licensed Real estate agent</div>

    <section class="letter__body">
      <p class="salutation">Dear Home Owner</p>
      <p>I am writing you because I am interested in purchasing your property located at <strong>207 NE Willowbrook Ave LAKEVIEW FL.</strong> I live nearby in Cedarbrook and I Purchase properties throughout the state of Flordia. Currently I am working on projects in the neighborhood, which is how I learned of your property.</p>
      <p>Please call me at . So i can tell you how we can buy your property quickly, with no hassles and most importantly, at a fair price. I purchase the house directly from you, so there are no real estate commissions or extr fees coming out of your pocket. Furthermore, I always make cash offers so you never have to worry about delays resulting from a buyer trying to quality for a morgage and wastingyour valuble time.</p>
      <p>I'll be glad to personally tell you more about how we can work together. All calls are completely confidential and there is no obligation whatsoever. Even if you are not inteested in selling at this time call (352) 555-0148. So i can help you with derermining the value of your property. You should also keep this letter for further reference. since things in life have a tendency to chagne unexpectedly. Thank you for your time and consideration and I look forward to speaking with you.</p>
    </section>

    <div class="letter__closing">Sincerely,</div>
    <div class="signature-mark" role="img" aria-label="Handwritten signature"></div>
    <div class="signer">
      <div class="signer__name">Dana Whitfield</div>
      <div class="signer__phone">(352)555-0148</div>
    </div>

    <div class="letter__block postscript">
      P.S. If you would like to e-mail me<br>
      information and pictures of your property.<br>
      please send them to dana@porchkey.com
    </div>

    <div class="mascot-photo" role="img" aria-label="Photo of a smiling white bulldog wearing a red bandana"></div>
  </main>
</body>
</html>
```